Word Page Templates x 5

1 x Letterhead Template with Header and Footer able to be printed to paper and pdf with non blurry resolution
- File attached looks ok on computer screen but does not print the same
- We are wanting it to print like it looks on the screen
- We are wanting it to print not fuzzy in resolution
- We are wanting the banner to be on the absolute edge of the page like it is on the computer screen
- We are needing to print this to paper and pdf with perfect resolution and colour

Please can someone help us!!

I have provided the logo files in our posession. If better resolutions are required please let us know.

We are also wanting 4 simple page templates to be setup in Landscape and Portrait orientation as well once we are happy with the letterhead that is provided samples have been provided
Updates

Hi all I have the vector files available now along with a Colour profile

Requirements
Must have
• Clear when printed on A4 Paper
Should not have
• Blurry images, Colour must be correct (same as Logo) - Please reference our website if need be ..... vornal.com.au

```html
<!DOCTYPE html>
<html lang="en">
<head>
<meta charset="utf-8">
<title>Vornal Pavement Services – Page Templates</title>
<link href="https://fonts.googleapis.com/css2?family=Source+Sans+3:wght@400;600;800&display=swap" rel="stylesheet">
<style>
  :root {
    --backdrop: #177d86;
    --paper: #ffffff;
    --brand-green: #1b7a3e;
    --brand-navy: #1f3a86;
    --tagline-grey: #6b6b6b;
    --badge-tone: #c9d3e6;
  }
  * { margin: 0; padding: 0; box-sizing: border-box; }
  html, body { width: 1200px; height: 1200px; overflow: hidden; }
  body {
    background: var(--backdrop);
    position: relative;
    font-family: "Source Sans 3", "Myriad Pro", sans-serif;
  }
  .page {
    position: absolute;
    background: var(--paper);
    box-shadow: 0 1px 3px rgba(0,0,0,0.25);
    overflow: hidden;
  }
  .page--portrait { width: 340px; height: 480px; top: 110px; }
  .page--landscape { width: 534px; height: 377px; top: 698px; }
  .page--a { left: 46px; }
  .page--b { left: 432px; }
  .page--c { left: 817px; }
  .page--d { left: 42px; }
  .page--e { left: 619px; }

  .edge-band {
    position: absolute; left: 0; right: 0; height: 13px;
  }
  .edge-band--top { top: 0; }
  .edge-band--bottom { bottom: 0; }
  .edge-band__solid {
    position: absolute; left: 0; right: 0; height: 5px;
    background: linear-gradient(90deg, var(--brand-green), var(--brand-navy));
  }
  .edge-band__pattern {
    position: absolute; left: 0; right: 0; height: 5px;
    background: linear-gradient(90deg, #7fb592, #8f9fc8);
  }
  .edge-band--top .edge-band__solid { top: 0; }
  .edge-band--top .edge-band__pattern { top: 7px; }
  .edge-band--bottom .edge-band__solid { bottom: 0; }
  .edge-band--bottom .edge-band__pattern { bottom: 7px; }

  .wordmark { position: absolute; line-height: 1; }
  .wordmark__name {
    display: block;
    font-weight: 800;
    color: var(--brand-green);
    letter-spacing: 0.5px;
  }
  .wordmark__tagline {
    display: block;
    color: var(--tagline-grey);
    font-weight: 600;
    letter-spacing: 0.6px;
    text-align: right;
  }
  .wordmark--large .wordmark__name { font-size: 33px; }
  .wordmark--large .wordmark__tagline { font-size: 7.5px; margin-top: 1px; }
  .wordmark--medium .wordmark__name { font-size: 26px; }
  .wordmark--medium .wordmark__tagline { font-size: 5px; margin-top: 1px; }
  .wordmark--small .wordmark__name { font-size: 18px; }
  .wordmark--small .wordmark__tagline { font-size: 3.4px; margin-top: 1px; }

  .contact-list {
    position: absolute; list-style: none;
    color: var(--brand-navy); line-height: 1.5;
  }
  .contact-list--portrait { font-size: 5.5px; left: 226px; top: 30px; }
  .contact-list--landscape { font-size: 6.6px; left: 424px; top: 28px; }
  .contact-list__key { color: var(--brand-green); display: inline-block; width: 1.6em; }

  .affiliations { position: absolute; left: 22px; top: 417px; width: 296px; height: 36px; }
  .affiliations__rule { position: absolute; top: 0; height: 2px; }
  .affiliations__rule--navy { left: 0; width: 215px; background: var(--brand-navy); }
  .affiliations__rule--green { left: 230px; width: 66px; background: var(--brand-green); }
  .affiliations__caption {
    position: absolute; top: 8px; left: 0;
    font-size: 5px; color: var(--brand-navy); text-transform: uppercase;
  }
  .affiliations__badge {
    position: absolute; top: 20px; height: 16px; background: var(--badge-tone); border-radius: 2px;
  }
</style>
</head>
<body>

  <!-- Portrait letterhead with affiliations footer -->
  <section class="page page--portrait page--a">
    <div class="edge-band edge-band--top">
      <div class="edge-band__solid"></div>
      <div class="edge-band__pattern" role="img" aria-label="Green to navy chevron border pattern"></div>
    </div>
    <div class="wordmark wordmark--large" style="left:21px; top:29px;">
      <span class="wordmark__name">VORNAL</span>
      <span class="wordmark__tagline">PAVEMENT SERVICES</span>
    </div>
    <ul class="contact-list contact-list--portrait">
      <li><span class="contact-list__key">A.</span>PO Box 2290, Kestrel Bay Qld 4580</li>
      <li><span class="contact-list__key">P.</span>07 4418 209</li>
      <li><span class="contact-list__key">E.</span>admin@vornal.com.au</li>
      <li><span class="contact-list__key">W.</span>www.vornal.com.au</li>
    </ul>
    <div class="affiliations">
      <div class="affiliations__rule affiliations__rule--navy"></div>
      <div class="affiliations__rule affiliations__rule--green"></div>
      <p class="affiliations__caption">Vornal Pavement Services are proudly affiliated with</p>
      <div class="affiliations__badge" style="left:0; width:60px;" role="img" aria-label="Partner badge"></div>
      <div class="affiliations__badge" style="left:67px; width:26px;" role="img" aria-label="Association badge"></div>
      <div class="affiliations__badge" style="left:100px; width:22px;" role="img" aria-label="Membership badge"></div>
      <div class="affiliations__badge" style="left:129px; width:24px;" role="img" aria-label="Certification badge"></div>
    </div>
    <div class="wordmark wordmark--small" style="left:258px; top:437px;">
      <span class="wordmark__name">VORNAL</span>
      <span class="wordmark__tagline">PAVEMENT SERVICES</span>
    </div>
    <div class="edge-band edge-band--bottom">
      <div class="edge-band__pattern" role="img" aria-label="Green to navy chevron border pattern"></div>
      <div class="edge-band__solid"></div>
    </div>
  </section>

  <!-- Portrait letterhead, header only -->
  <section class="page page--portrait page--b">
    <div class="edge-band edge-band--top">
      <div class="edge-band__solid"></div>
      <div class="edge-band__pattern" role="img" aria-label="Green to navy chevron border pattern"></div>
    </div>
    <div class="wordmark wordmark--large" style="left:21px; top:29px;">
      <span class="wordmark__name">VORNAL</span>
      <span class="wordmark__tagline">PAVEMENT SERVICES</span>
    </div>
    <ul class="contact-list contact-list--portrait">
      <li><span class="contact-list__key">A.</span>PO Box 2290, Kestrel Bay Qld 4580</li>
      <li><span class="contact-list__key">P.</span>07 4418 209</li>
      <li><span class="contact-list__key">E.</span>admin@vornal.com.au</li>
      <li><span class="contact-list__key">W.</span>www.vornal.com.au</li>
    </ul>
    <div class="edge-band edge-band--bottom">
      <div class="edge-band__pattern" role="img" aria-label="Green to navy chevron border pattern"></div>
      <div class="edge-band__solid"></div>
    </div>
  </section>

  <!-- Portrait continuation page -->
  <section class="page page--portrait page--c">
    <div class="edge-band edge-band--top">
      <div class="edge-band__solid"></div>
      <div class="edge-band__pattern" role="img" aria-label="Green to navy chevron border pattern"></div>
    </div>
    <div class="wordmark wordmark--medium" style="left:231px; top:429px;">
      <span class="wordmark__name">VORNAL</span>
      <span class="wordmark__tagline">PAVEMENT SERVICES</span>
    </div>
    <div class="edge-band edge-band--bottom">
      <div class="edge-band__pattern" role="img" aria-label="Green to navy chevron border pattern"></div>
      <div class="edge-band__solid"></div>
    </div>
  </section>

  <!-- Landscape letterhead -->
  <section class="page page--landscape page--d">
    <div class="edge-band edge-band--top">
      <div class="edge-band__solid"></div>
      <div class="edge-band__pattern" role="img" aria-label="Green to navy chevron border pattern"></div>
    </div>
    <div class="wordmark wordmark--large" style="left:20px; top:28px;">
      <span class="wordmark__name">VORNAL</span>
      <span class="wordmark__tagline">PAVEMENT SERVICES</span>
    </div>
    <ul class="contact-list contact-list--landscape">
      <li><span class="contact-list__key">A.</span>PO Box 2290, Kestrel Bay Qld 4580</li>
      <li><span class="contact-list__key">P.</span>07 4418 209</li>
      <li><span class="contact-list__key">E.</span>admin@vornal.com.au</li>
      <li><span class="contact-list__key">W.</span>www.vornal.com.au</li>
    </ul>
    <div class="edge-band edge-band--bottom">
      <div class="edge-band__pattern" role="img" aria-label="Green to navy chevron border pattern"></div>
      <div class="edge-band__solid"></div>
    </div>
  </section>

  <!-- Landscape continuation page -->
  <section class="page page--landscape page--e">
    <div class="edge-band edge-band--top">
      <div class="edge-band__solid"></div>
      <div class="edge-band__pattern" role="img" aria-label="Green to navy chevron border pattern"></div>
    </div>
    <div class="wordmark wordmark--medium" style="left:427px; top:316px;">
      <span class="wordmark__name">VORNAL</span>
      <span class="wordmark__tagline">PAVEMENT SERVICES</span>
    </div>
    <div class="edge-band edge-band--bottom">
      <div class="edge-band__pattern" role="img" aria-label="Green to navy chevron border pattern"></div>
      <div class="edge-band__solid"></div>
    </div>
  </section>

</body>
</html>
```